Interfaith organization needs a poster advertising event for youth

We need a poster advertising our annual Lantern Gathering and Summit, where youth of all different religions come together for dialogue, friendship, fun, art, and musical performances. The poster should be have a front advertising the event, and the back should have more detailed descriptions of the event and submissions. It should be fun and eye catching!

Target Market(s)

Youth and Religious Organizations

Industry/Entity Type

Festival

Font styles to use
Serif

Requirements
Must have
• Pictures, poster-feel, contact information, etc. Logos of Bright Harbor Allies and Crossroads Young Leaders Circle of Maple Valley

```html
<!DOCTYPE html>
<html lang="en">
<head>
<meta charset="utf-8">
<title>Crossroads Young Leaders Circle – 13th Annual Lantern Gathering &amp; Summit</title>
<link rel="stylesheet" href="https://fonts.googleapis.com/css2?family=Montserrat:ital,wght@0,400;0,500;0,700;0,800;1,400;1,700;1,800&family=Playfair+Display:ital,wght@1,400&display=swap">
<style>
  :root {
    --red: #e2404a;
    --yellow: #fdd117;
    --blue: #4a8dcc;
    --green: #3fb54d;
    --purple: #5d55a5;
    --ink: #1f1f1f;
    --grey: #7d7d7d;
    --white: #ffffff;
  }
  * { margin: 0; padding: 0; box-sizing: border-box; }
  html, body { width: 927px; height: 1200px; overflow: hidden; background: var(--white); }
  .poster {
    position: relative; width: 927px; height: 1200px; overflow: hidden;
    font-family: "Montserrat", Arial, sans-serif; color: var(--ink);
  }
  .masthead {
    position: absolute; left: 0; top: 0; width: 927px; height: 148px;
    background: var(--red); color: var(--white); text-align: center;
  }
  .masthead .org {
    font-family: "Playfair Display", Georgia, serif; font-style: italic;
    font-size: 25px; padding-top: 22px; line-height: 1;
  }
  .masthead .title {
    font-weight: 800; font-size: 34.5px; line-height: 1; margin-top: 12px; letter-spacing: -0.2px;
  }
  .masthead .tagline {
    font-family: "Playfair Display", Georgia, serif; font-style: italic;
    font-size: 18px; margin-top: 12px;
  }
  .masthead .tagline b {
    font-family: "Montserrat", Arial, sans-serif; font-style: normal; font-weight: 800; font-size: 19px;
  }
  .stripe { position: absolute; left: 0; width: 927px; display: flex; }
  .stripe span { display: block; height: 100%; }
  .stripe-top { top: 148px; height: 21px; }
  .stripe-bottom { top: 435px; height: 22px; }
  .yellow { background: var(--yellow); } .blue { background: var(--blue); }
  .green { background: var(--green); } .purple { background: var(--purple); }
  .red { background: var(--red); }

  .event-photo {
    position: absolute; left: 527px; top: 169px; width: 400px; height: 266px;
    background: linear-gradient(160deg, #8f86c6 0%, #5a4f9c 45%, #2f2766 100%);
  }
  .event-info { position: absolute; left: 37px; top: 210px; width: 450px; }
  .event-info h1 {
    color: var(--purple); font-weight: 800; font-size: 29px; line-height: 1; letter-spacing: 0.2px;
  }
  .event-info .question {
    color: var(--purple); font-family: "Playfair Display", Georgia, serif; font-style: italic;
    font-size: 21px; margin-top: 6px;
  }
  .event-info .rule { height: 9px; width: 447px; background: var(--purple); margin-top: 10px; }
  .event-info .when { font-weight: 500; font-size: 19.5px; margin-top: 24px; }
  .event-info .when sup { font-size: 11px; }
  .event-info .where { font-size: 18.5px; margin-top: 10px; }
  .event-info .address { font-style: italic; font-size: 18px; margin-top: 6px; }

  .column { position: absolute; width: 402px; font-size: 15.3px; line-height: 24px; }
  .col-left { left: 43px; top: 496px; }
  .col-right { left: 485px; top: 493px; }
  .intro { font-style: italic; }
  .intro b { font-weight: 800; }
  .section-head { font-weight: 800; font-size: 20px; line-height: 1; letter-spacing: 0.2px; }
  .section-head.purple-text { color: var(--purple); }
  .section-head.red-text { color: var(--red); }
  .section-head.blue-text { color: var(--blue); }
  .section-rule { height: 9px; width: 402px; margin: 5px 0 8px; }
  .rsvp { font-weight: 800; font-style: italic; text-decoration: underline; margin-top: 5px; }
  .rsvp sup { font-size: 9px; }
  .indent { text-indent: 24px; }

  .partners { position: absolute; top: 1062px; left: 590px; display: flex; align-items: center; gap: 30px; }
  .partner { display: flex; align-items: center; gap: 10px; color: var(--grey); font-weight: 500; }
  .partner-mark { width: 46px; height: 46px; border-radius: 50%; border: 2px solid var(--grey); flex: none; }
  .partner-name { font-size: 15px; line-height: 18px; }
  .partner-wide .partner-name { width: 120px; font-size: 13px; line-height: 16px; }
</style>
</head>
<body>
<div class="poster">
  <header class="masthead">
    <p class="org">Crossroads Young Leaders Circle of Maple Valley's</p>
    <p class="title">13th Annual Lantern Gathering &amp; Summit</p>
    <p class="tagline">“teens expressing their faith through <b>ART, MUSIC, AND DIALOGUE”</b></p>
  </header>
  <div class="stripe stripe-top">
    <span class="yellow" style="width:233px"></span><span class="blue" style="width:232px"></span>
    <span class="green" style="width:232px"></span><span class="purple" style="width:230px"></span>
  </div>

  <section class="event-info">
    <h1>INTERFAITH YOUTH FORUM</h1>
    <p class="question">“Is Religion Cool?"</p>
    <div class="rule"></div>
    <p class="when">Sunday March 19<sup>th</sup>, 2017 &nbsp;/&nbsp; 11am - 5pm</p>
    <p class="where">@ The Willowbrook Fellowship Hall</p>
    <p class="address">4150 Orchard Lane, Maple Valley, CA 90000</p>
  </section>
  <div class="event-photo" role="img" aria-label="Photo of teens seated around round tables in discussion at a past forum, tinted purple"></div>

  <div class="stripe stripe-bottom">
    <span class="purple" style="width:183px"></span><span class="green" style="width:187px"></span>
    <span class="blue" style="width:187px"></span><span class="red" style="width:186px"></span>
    <span class="yellow" style="width:184px"></span>
  </div>

  <section class="column col-left">
    <p class="intro">All high school age faith groups are invited to come and join with 150 to 175 other high school students from various faith traditions to participate in the <b>Crossroads Young Leaders Circle of Maple Valley's Annual Interfaith Youth Forum</b>. More than ever, our county and world need young leaders who are willing to learn from each other and <b>build stronger communities!</b></p>
    <h2 class="section-head purple-text" style="margin-top:28px">LANTERN SUMMIT</h2>
    <div class="section-rule purple"></div>
    <p>The purpose of this Interfaith Youth Forum is to bring together young people from diverse ethnic, cultural, and religious backgrounds, and to engage them in dialogue. True dialogue is a conversation on a common subject between two or more persons of differing points of view and/or backgrounds. We feel that this commitment to dialogue will affect relationships in a constructive way in our places of worship and in our community.</p>
    <p class="indent">The forum itself involves having eight religiously diverse high school-age students, one adult, and youth leader around each table to discuss common questions. Our youth leaders act as facilitators, but it is stressed that it is the students we want to hear from.</p>
    <p class="rsvp">RSVP for our LANTERN SUMMIT by February 19<sup>th</sup>, 2017</p>
  </section>

  <section class="column col-right">
    <h2 class="section-head red-text">LANTERN GATHERING</h2>
    <div class="section-rule red"></div>
    <p>The forum will be followed by the Lantern Gathering where families of the participants are welcomed to join. The Gathering will include musical performances of all types from diverse religious communities. The differing performing arts include but are not limited to singing, dancing, instrumental music, storytelling, etc.</p>
    <p class="rsvp">To Participate in our Lantern Gathering (Music, Song, Dance), RSVP by February 25<sup>th</sup>, 2017</p>
    <h2 class="section-head blue-text" style="margin-top:44px">ART GALLERY</h2>
    <div class="section-rule blue"></div>
    <p>This event will include and Art Gallery display of students' work, highlighting their expressions of faith, and artwork promoting learning, understanding, leadership, and service. Art includes any painting, illustration, sculpture, photography or other visual art.</p>
    <p class="rsvp">Art Work for our Art Galley must be submitted by: March 10<sup>th</sup>, 2017</p>
  </section>

  <footer class="partners">
    <div class="partner"><span class="partner-name">Bright Harbor<br>Allies</span></div>
    <div class="partner partner-wide"><span class="partner-mark"></span><span class="partner-name">Crossroads Young Leaders Circle of Maple Valley</span></div>
  </footer>
</div>
</body>
</html>
```